Bed Company needs business card

Hello, we are a bed company that makes specialized magnets for beds. We are an alternative healing company. I need a modern and upscale business card. Please incorporate my logo for the card.

Accepted file formats are AI, EPS, and Press-Ready PDFS.

Please include all fonts or convert them to outlines regardless of file type.

If you are designing the card in Photoshop the file Must be 1200dpi.

I am open to anything for the business card.  I really like all of your designs and if you want to change the color of the logo, you can.  I will be making the final selection by Friday.  Thank You for all of your designs.  Feel Free to submit different color logos if you want.  

Reason: I will make a decision Final on Friday April 20th. 2012. Good Luck and Thank you all for the designs.

Target Market(s)

My target Market is people, who are looking for alternative healing.

Industry/Entity Type

Business

Requirements
Must have
• My logo must be incorporated. The front card must have

Name
Job Title

Address
Work
Cell
Fax
email
web

Just put in fake info for the card.

The back of the card. I want the logo on the back with color. I just want it to look modern and cool.

```html
<!DOCTYPE html>
<html lang="en">
<head>
<meta charset="utf-8">
<title>Lodestar Rest – Business Card</title>
<link href="https://fonts.googleapis.com/css2?family=Barlow:wght@400;500&display=swap" rel="stylesheet">
<style>
  :root {
    --page: #ffffff;
    --card-dark: #242424;
    --card-mid: #333333;
    --rule-light: #ffffff;
    --rule-dark: #050505;
    --ink: #ffffff;
    --label: #6a6a6a;
    --glow: #b5b5b5;
  }
  * { margin: 0; padding: 0; box-sizing: border-box; }
  html, body {
    width: 940px; height: 1200px; overflow: hidden;
    background: var(--page);
    font-family: "Barlow", Arial, sans-serif;
  }
  .canvas { position: relative; width: 940px; height: 1200px; }

  .card { position: absolute; overflow: hidden; }

  .card-front {
    left: 9px; top: 3px; width: 925px; height: 564px;
    background: linear-gradient(90deg, var(--card-mid) 0%, var(--card-dark) 45%, var(--card-dark) 100%);
  }
  .rule { position: absolute; }
  .rule-v-dark  { left: 64px; top: 0; width: 11px; height: 100%; background: var(--rule-dark); }
  .rule-v-light { left: 97px; top: 0; width: 6px;  height: 100%; background: var(--rule-light); }
  .rule-h-top   { left: 0; top: 71px; width: 100%; height: 6px; background: var(--rule-light); }
  .rule-h-bottom{ left: 0; top: 85px; width: 100%; height: 6px; background: var(--rule-light); }
  .rule-h-gap   { left: 0; top: 77px; width: 100%; height: 8px; background: var(--rule-dark); }

  .brand { position: absolute; display: flex; align-items: center; color: var(--ink); }
  .brand-mark { border: 3px solid var(--ink); flex: none; }
  .brand-text { display: flex; flex-direction: column; }
  .brand-name { font-weight: 500; line-height: 1; letter-spacing: 0.5px; }
  .brand-tagline { font-weight: 500; letter-spacing: 3px; line-height: 1; }

  .card-front .brand { left: 470px; top: 150px; gap: 18px; }
  .card-front .brand-mark { width: 70px; height: 70px; }
  .card-front .brand-name { font-size: 44px; }
  .card-front .brand-tagline { font-size: 14px; margin-top: 6px; }

  .contact {
    position: absolute; left: 115px; top: 408px;
    display: grid; grid-template-columns: 67px auto; row-gap: 13px;
    font-size: 13px; line-height: 19px; font-weight: 500;
  }
  .contact dt { color: var(--label); }
  .contact dd { color: var(--ink); letter-spacing: 0.3px; }

  .card-back {
    left: 0; top: 628px; width: 928px; height: 566px;
    background: radial-gradient(circle at 452px 268px, var(--glow) 0%, #6e6e6e 22%, #3a3a3a 45%, var(--card-dark) 70%);
  }
  .card-back .brand { left: 170px; top: 205px; gap: 26px; }
  .card-back .brand-mark { width: 110px; height: 110px; border-width: 4px; }
  .card-back .brand-name { font-size: 76px; }
  .card-back .brand-tagline { font-size: 24px; margin-top: 8px; }
</style>
</head>
<body>
<main class="canvas">

  <section class="card card-front" aria-label="Business card front">
    <div class="rule rule-h-gap"></div>
    <div class="rule rule-h-top"></div>
    <div class="rule rule-h-bottom"></div>
    <div class="rule rule-v-dark"></div>
    <div class="rule rule-v-light"></div>

    <div class="brand">
      <span class="brand-mark" aria-hidden="true"></span>
      <div class="brand-text">
        <span class="brand-name">Lodestar Rest</span>
        <span class="brand-tagline">Alternative Healing</span>
      </div>
    </div>

    <dl class="contact">
      <dt>Name</dt><dd>Jordan Hale</dd>
      <dt>Address</dt><dd>No 5, Elm Row, Fairview</dd>
      <dt>Contact</dt><dd>555 0148 220 000</dd>
      <dt>Fax</dt><dd>555 0148 220 777</dd>
      <dt>Email</dt><dd>hello@lodestarrest.example</dd>
    </dl>
  </section>

  <section class="card card-back" aria-label="Business card back">
    <div class="brand">
      <span class="brand-mark" aria-hidden="true"></span>
      <div class="brand-text">
        <span class="brand-name">Lodestar Rest</span>
        <span class="brand-tagline">Alternative Healing</span>
      </div>
    </div>
  </section>

</main>
</body>
</html>
```